Global Nano Technology Surface Protection company needs a new logo and cards

We are a Global company that will apply nanotechnology coatings on surfaces to prevent growth and spread of bacteria, viruses, mold etc. We deal with large corporates, airlines, hospitals and schools so we are after a new modern, simple and clean look that will have great visual impact.
We a company that is focused on prevention and protection.

Company name, Quorvane Systems Worldwide

Subtext, Antimicrobial Surface Protection

Logo, QVSW or QSW

Target Market(s)

Hospitals, Transport agencies, Airlines, Corporate entities

Industry/Entity Type

Protection

Contact Information for Business Card

Logo, QVSW or QSW
www.qvsw-example.us
Derek Holloway
+64290536218
tidyshieldnz@mailbox-example.com

Logo Text

QVSW

Requirements
Must have
• Simple clean look
Should not have
• Nothing too messy

```html
<!DOCTYPE html>
<html lang="en">
<head>
<meta charset="utf-8">
<title>Quorvane Systems Worldwide — Business Cards</title>
<link rel="stylesheet" href="https://fonts.googleapis.com/css2?family=Roboto:wght@400;700&family=Montserrat:wght@400&display=swap">
<style>
  :root {
    --backdrop: #d3d7d9;
    --card: #f1f1ef;
    --ink: #4a4b4f;
    --ink-soft: #66676b;
    --accent: #1aa6ea;
    --edge: #1b8fd6;
  }
  * { margin: 0; padding: 0; box-sizing: border-box; }
  html, body { width: 1200px; height: 852px; overflow: hidden; }
  body {
    background: var(--backdrop);
    display: flex;
    flex-direction: column;
    align-items: center;
    justify-content: center;
    gap: 36px;
    font-family: "Roboto", Arial, sans-serif;
    color: var(--ink);
  }
  .card {
    width: 640px;
    height: 366px;
    background: var(--card);
    border-bottom: 4px solid var(--edge);
    box-shadow: 0 6px 18px rgba(0,0,0,0.12);
    position: relative;
    display: flex;
    align-items: center;
  }

  /* Name placeholder where the mark stands */
  .brand-name {
    font-family: "Roboto", Arial, sans-serif;
    font-weight: 400;
    color: var(--ink);
    line-height: 1;
    white-space: nowrap;
  }

  /* Company lockup */
  .company { line-height: 1.1; }
  .company-line1 {
    font-weight: 700;
    color: var(--ink);
    white-space: nowrap;
  }
  .company-line2 {
    display: flex;
    align-items: center;
    gap: 8px;
    color: var(--ink);
    font-weight: 400;
  }
  .rule-pair {
    display: flex;
    flex-direction: column;
    gap: 3px;
    flex: 1;
  }
  .rule-pair span { height: 2px; background: var(--accent); display: block; }
  .tagline {
    font-family: "Montserrat", Arial, sans-serif;
    text-transform: uppercase;
    color: var(--ink-soft);
    letter-spacing: 0.5px;
    white-space: nowrap;
  }

  /* Front */
  .card-front { padding-left: 60px; }
  .card-front .brand-name { font-size: 52px; width: 180px; }
  .divider {
    width: 2px;
    height: 200px;
    background: var(--accent);
    margin: 0 26px 0 30px;
  }
  .details { width: 290px; }
  .card-front .company-line1 { font-size: 21px; }
  .card-front .company-line2 { font-size: 21px; margin-top: 2px; }
  .card-front .tagline { font-size: 10px; margin-top: 5px; }
  .person {
    font-size: 27px;
    color: var(--accent);
    font-weight: 400;
    margin: 14px 0 12px;
  }
  .contacts { list-style: none; font-family: "Montserrat", Arial, sans-serif; font-size: 13.5px; color: var(--ink); }
  .contacts li { display: flex; align-items: center; gap: 9px; margin-bottom: 6px; white-space: nowrap; }
  .contacts svg { width: 13px; height: 13px; flex: none; }

  /* Back */
  .card-back { justify-content: center; }
  .back-lockup { display: flex; flex-direction: column; align-items: center; }
  .card-back .brand-name { font-size: 72px; }
  .card-back .company { width: 290px; margin-top: 18px; }
  .card-back .company-line1 { font-size: 22px; text-align: center; }
  .card-back .company-line2 { font-size: 22px; margin-top: 2px; }
  .card-back .tagline { font-size: 10.5px; margin-top: 6px; text-align: center; }
</style>
</head>
<body>

  <section class="card card-front" aria-label="Business card front">
    <div class="brand-name">QVSW</div>
    <div class="divider"></div>
    <div class="details">
      <div class="company">
        <div class="company-line1">Quorvane Systems</div>
        <div class="company-line2">
          <span class="rule-pair"><span></span><span></span></span>
          <span>Worldwide</span>
          <span class="rule-pair"><span></span><span></span></span>
        </div>
        <div class="tagline">Antimicrobial Surface Protection</div>
      </div>
      <div class="person">Derek Holloway</div>
      <ul class="contacts">
        <li>
          <svg viewBox="0 0 16 16" aria-hidden="true"><path fill="var(--accent)" d="M3.6 1.2l2.3 2.9-1.3 1.6c.9 2 2.6 3.7 4.6 4.6l1.6-1.3 2.9 2.3-1.5 2.2C7.4 13.3 2.7 8.6 1.4 3z"/></svg>
          +64290536218
        </li>
        <li>
          <svg viewBox="0 0 16 16" aria-hidden="true"><rect x="1.5" y="3.5" width="13" height="9" fill="none" stroke="var(--accent)" stroke-width="1.6"/><path d="M1.5 3.5L8 9l6.5-5.5" fill="none" stroke="var(--accent)" stroke-width="1.6"/></svg>
          tidyshieldnz@mailbox-example.com
        </li>
        <li>
          <svg viewBox="0 0 16 16" aria-hidden="true"><circle cx="8" cy="8" r="6.5" fill="none" stroke="var(--accent)" stroke-width="1.5"/><ellipse cx="8" cy="8" rx="2.8" ry="6.5" fill="none" stroke="var(--accent)" stroke-width="1.2"/><path d="M1.5 8h13M2.5 5h11M2.5 11h11" stroke="var(--accent)" stroke-width="1.1"/></svg>
          www.qvsw-example.us
        </li>
      </ul>
    </div>
  </section>

  <section class="card card-back" aria-label="Business card back">
    <div class="back-lockup">
      <div class="brand-name">QVSW</div>
      <div class="company">
        <div class="company-line1">Quorvane Systems</div>
        <div class="company-line2">
          <span class="rule-pair"><span></span><span></span></span>
          <span>Worldwide</span>
          <span class="rule-pair"><span></span><span></span></span>
        </div>
        <div class="tagline">Antimicrobial Surface Protection</div>
      </div>
    </div>
  </section>

</body>
</html>
```